Sing Across The Harbor redesign book cover

A new cover for my already published book. The old cover looks great but not for a women’s self help book. Cover is killing sales. Once I explain the book it sells quickly AND gets 5 star reviews. Outside of actually explaining the book the cover scares people away. I need a new cover. ASAP! Before The yr end please.
The tag line -
Discover 10 Practical Ways To Replace negative thoughts with knowing the voice of God. This is a self help book for women 35-45 Christian but not religious. Each chapter is a hands on spiritual experience where the reader takes small tests about themselves, discover why they have negative thoughts, what they are and how to listen to God through hands on methods of listening. NOT strange type of things. They learn what 4 voices they are listening to and how to hone in on Jesus voice. There are scriptures to pray and journaling assignments. The old cover is in the brief with the write up for the back of the book. Please use the new author picture, Publishers logo (tree), barcode, and contact info from the back of the book. And yes the author name and title of the book on the spine. Lay out on the back cover needs to be interesting. You have all the info have fun with it.

Target Market(s)

Women 35-45 yrs old Christian and new believers or seekers.

Industry/Entity Type

Non profit organization. Missionary

Requirements
Must have
• Something DIFFERENT than what is there now. Something inviting. Fresh clear title
Nice to have
• Multi colors however a white stand out cover is also good.
Should not have
• Heavy religious feeling. No church steeples, Jesus faces.

```html
<!DOCTYPE html>
<html lang="en">
<head>
<meta charset="utf-8">
<title>Sing Across The Harbor — Cover</title>
<link rel="stylesheet" href="https://fonts.googleapis.com/css2?family=DM+Serif+Display&family=Inter:wght@600;700&display=swap">
<style>
  :root {
    --backdrop: #b0a6a2;
    --paper: #eae0d0;
    --title-red: #e8423f;
    --white: #ffffff;
    --author-ink: #4a403c;
    --rock-blue: #6f8088;
    --rock-mid: #9a8f80;
    --rock-moss: #8f9652;
    --stone-light: #b8b0aa;
    --stone-dark: #8c837e;
  }
  * { margin: 0; padding: 0; box-sizing: border-box; }
  html, body {
    width: 1200px; height: 1200px; overflow: hidden;
    background: var(--backdrop);
  }
  .cover {
    position: absolute;
    left: 275px; top: 112px;
    width: 651px; height: 976px;
    background: var(--paper);
    overflow: hidden;
  }
  .cover-art { position: absolute; left: 0; top: 0; }
  .tagline {
    position: absolute;
    left: 44px; top: 48px;
    font-family: "Inter", sans-serif;
    font-weight: 600;
    font-size: 19px;
    line-height: 27px;
    letter-spacing: -0.3px;
    color: var(--white);
  }
  .title {
    position: absolute;
    left: 36px; top: 150px;
    font-family: "DM Serif Display", serif;
    font-weight: 400;
    font-size: 146px;
    line-height: 148px;
    letter-spacing: -3px;
    color: var(--title-red);
  }
  .title span { display: block; }
  .author {
    position: absolute;
    left: 38px; top: 890px;
    font-family: "Inter", sans-serif;
    font-weight: 700;
    font-size: 36px;
    letter-spacing: -0.6px;
    color: var(--author-ink);
  }
</style>
</head>
<body>
  <div class="cover">
    <svg class="cover-art" width="651" height="976" viewBox="0 0 651 976">
      <defs>
        <linearGradient id="rockTone" x1="0" y1="0" x2="1" y2="0">
          <stop offset="0" stop-color="var(--rock-blue)"/>
          <stop offset="0.5" stop-color="var(--rock-mid)"/>
          <stop offset="1" stop-color="var(--rock-moss)"/>
        </linearGradient>
        <linearGradient id="rockFade" x1="0" y1="0" x2="0" y2="1">
          <stop offset="0" stop-color="#fff" stop-opacity="1"/>
          <stop offset="0.55" stop-color="#fff" stop-opacity="0.85"/>
          <stop offset="1" stop-color="#fff" stop-opacity="0"/>
        </linearGradient>
        <mask id="rockMask">
          <rect width="651" height="470" fill="url(#rockFade)"/>
        </mask>
        <radialGradient id="stoneTone" cx="0.62" cy="0.7" r="0.6">
          <stop offset="0" stop-color="var(--stone-light)" stop-opacity="0.95"/>
          <stop offset="0.6" stop-color="var(--stone-dark)" stop-opacity="0.6"/>
          <stop offset="1" stop-color="var(--stone-dark)" stop-opacity="0"/>
        </radialGradient>
      </defs>
      <rect role="img" aria-label="Upside-down photograph of rocky mountain peaks with green slopes across the top of the cover"
            x="0" y="0" width="651" height="470" fill="url(#rockTone)" mask="url(#rockMask)"/>
      <rect role="img" aria-label="Photograph of a classical marble statue of a woman looking upward, hand on her chest"
            x="110" y="440" width="541" height="536" fill="url(#stoneTone)"/>
    </svg>

    <p class="tagline">Discover 10 Practical Ways to<br>Replace Negative Thoughts<br>With Knowing the Voice Of God</p>

    <h1 class="title"><span>Sing</span><span>Across</span><span>The</span><span>Harbor</span></h1>

    <p class="author">Mara Ellison</p>
  </div>
</body>
</html>
```